Book Cover Design Project

I have written a booK called "Build From Nothing:
a handbook for launching and steering a modest enterprise. It is aimed at the start up entrepreneur and seeks to give them everything they need to start up and run a small business. I am interested in a very simple cover that is contemporary in the look but clearly communicates the mission of the book. It should sell very well as there are no others like it, so the designer will get excellent exposure.
Updates

Reason: I an vacation in Europe until the 23rd of July. Would like a few days to make a decision after my return Ned

We are currently on vacation.  Will make a final decision in about a week.  Thanks so much for your submissions

Ned

Target Market(s)

Start up businesses in the U.S.

Industry/Entity Type

Business

Requirements
Must have
• Clear communication of the name. Lots of white space. Graphic communication of the purpose of the book? Prominent exposure of my name. Edward r. Kistlewood

```html
<!DOCTYPE html>
<html lang="en">
<head>
<meta charset="utf-8">
<title>Build From Nothing — Edward R. Kistlewood</title>
<link rel="stylesheet" href="https://fonts.googleapis.com/css2?family=Courier+Prime:wght@400;700&display=swap">
<style>
  :root {
    --haze: #eef1f6;
    --sky: #c9d2e2;
    --steel: #8d9bb7;
    --navy: #2f3b5c;
    --ink: #0e1119;
    --sleeve: #2b3140;
    --skin: #bfb2a6;
    --piece-dark: #15171f;
    --piece-blue: #4c64a8;
    --rule: rgba(255, 255, 255, 0.9);
    --title-white: #ffffff;
    --title-glow: rgba(25, 40, 70, 0.8);
  }
  html, body {
    margin: 0;
    padding: 0;
    width: 800px;
    height: 1200px;
    overflow: hidden;
    background: #ffffff;
  }
  .cover {
    position: relative;
    width: 800px;
    height: 1200px;
    overflow: hidden;
    font-family: "Courier Prime", "Courier New", monospace;
  }
  .cover-photo {
    position: absolute;
    inset: 0;
    background:
      radial-gradient(ellipse 300px 260px at 50% 40%, rgba(191, 178, 166, 0.85), rgba(191, 178, 166, 0) 75%),
      radial-gradient(ellipse 220px 380px at 6% 38%, rgba(43, 49, 64, 0.95), rgba(43, 49, 64, 0) 78%),
      radial-gradient(ellipse 220px 360px at 96% 30%, rgba(35, 40, 55, 0.95), rgba(35, 40, 55, 0) 78%),
      radial-gradient(ellipse 90px 300px at 43% 88%, rgba(21, 23, 31, 0.95), rgba(21, 23, 31, 0) 80%),
      radial-gradient(ellipse 100px 290px at 58% 88%, rgba(76, 100, 168, 0.95), rgba(76, 100, 168, 0) 80%),
      radial-gradient(ellipse 200px 260px at 88% 85%, rgba(76, 100, 168, 0.8), rgba(76, 100, 168, 0) 78%),
      radial-gradient(ellipse 180px 300px at 8% 92%, rgba(25, 28, 38, 0.9), rgba(25, 28, 38, 0) 78%),
      radial-gradient(ellipse 420px 200px at 50% 10%, rgba(245, 247, 251, 1), rgba(245, 247, 251, 0) 75%),
      linear-gradient(180deg, var(--haze) 0%, var(--sky) 25%, var(--steel) 60%, var(--navy) 100%);
  }
  .author {
    position: absolute;
    top: 192px;
    left: 0;
    width: 800px;
    margin: 0;
    text-align: center;
    font-weight: 700;
    font-size: 36px;
    line-height: 48px;
    letter-spacing: 2px;
    color: var(--title-white);
    text-shadow:
      -1px -1px 0 #4a5266, 1px -1px 0 #4a5266,
      -1px 1px 0 #4a5266, 1px 1px 0 #4a5266;
  }
  .rule {
    position: absolute;
    left: 96px;
    width: 608px;
    height: 2px;
    background: var(--rule);
  }
  .rule-top { top: 255px; }
  .rule-bottom { top: 620px; }
  .title {
    position: absolute;
    top: 282px;
    left: 0;
    width: 800px;
    margin: 0;
    text-align: center;
    font-weight: 400;
    font-size: 110px;
    line-height: 160px;
    letter-spacing: 3px;
    color: var(--title-white);
    text-shadow:
      0 0 6px var(--title-glow),
      0 0 16px var(--title-glow),
      3px 3px 4px rgba(20, 28, 48, 0.6);
  }
  .subtitle {
    position: absolute;
    top: 636px;
    left: 0;
    width: 800px;
    margin: 0;
    text-align: center;
    font-size: 38px;
    line-height: 64px;
    color: var(--ink);
  }
</style>
</head>
<body>
  <main class="cover">
    <div class="cover-photo" role="img" aria-label="Photograph of two businessmen in dark suits shaking hands above a blue-tinted chessboard with a dark king and blue chess pieces"></div>
    <p class="author">EDWARD R.KISTLEWOOD</p>
    <div class="rule rule-top"></div>
    <h1 class="title">BUILD FROM<br>NOTHING</h1>
    <div class="rule rule-bottom"></div>
    <p class="subtitle">A handbook for launching and<br>steering a modest enterprise</p>
  </main>
</body>
</html>
```